依頼詳細
ぜひ頼んでみたい!!!と思ってくださるような
思い切りのいいランディングページをお願いいたします。

こんな資料がほしい!写真がほしい!動画もつけたい!
などがあればお気軽にお問い合わせください。
自由に最高のランディングページを作ってください。

参考はこちらのようなページですが
http://kumori-hitsuji.com/works/logodesign/
文字ばかりではなく、画像多めの
華やかでワクワクさせるような感じでお願いいたします。
「日本の美」を意識したデザインを希望します。
サイトURL
http://blog.tamarisu.jp/nekai/
ページ数
1ページ
希望イメージ
シンプル 複雑
単色 カラフル
暗い 明るい
日常 高級
遊び心 厳粛
未来的 伝統的
女性的 男性的
希望する色
日本をイメージさせる華やかなデザインをお願いいたします。
補足説明
ブログのロゴデザインのリンクから
今回作るランディングページへリンクしたいと考えています。
ランディングページ用の文章・画像
ご自由にブランディングして大丈夫です。
その場合は拝見させてください。
過去のブログの画像からも使って構いません。
http://fldr.example/7TxkWzR
サーバーはありますので、WEBデザインだけお願いいたします。
過去作品(インテリア用作品)
http://fldr.example/4GhvbQn

お仕事ロゴデザインサンプルなど
http://fldr.example/9JwcuLd

メディア掲載プロモーション用写真
http://fldr.example/2RpsyKe
素晴らしいデザインありがとうございました!!
どれも良いとおもっていまして
甲乙つけがたいです。
正直とても迷っているところで、延長させていただきました。

・インテリア作品
・ロゴデザインと
・プロフ写真も出します。
日本をイメージさせるデザインでお願いいたします。

ロゴデザインとインテリア用の作品が
混同されないようなご配慮をお願いいたします。
再開させていただきました。
華やかな日本をイメージさせるものにしたいです。
背景の一部に
・平安料紙切り継ぎ柄
・和紙柄
・着物柄
を取り入れて豪華なイメージにしていただきたいです。
ワークはロゴデザインを頼みたくなるような流れでお願いいたします。
金額の表示はやめることにします。
中盤や、最後に何回か
大きなボタンを入れてクリックしやすくしてほしいです。
どうぞよろしくお願いいたします。
平安調の継料紙が見当たらないとのご意見いただきました。
貴重なご意見をありがとうございます。

ワンポイントで
桜・和紙・千代紙・和柄・着物・着物帯柄など
素材がなければ無理のない程度でお願いいたします。

赤・桃色・日本を感じさせるようなデザインをお任せします。
下地背景は目に見やすい白を希望します。
ワークの順番やランディングの流れ等は
各自のデザインセンスにおまかせします。

メディア掲載も入れてもらってもかまいません。
お客様から信用を得られるようお願いしたいです。
経歴はブログをご覧ください。(抜粋して掲載を)

書道インテリア作品やロゴを多めに入れて、見栄え良くお願いします。
必要なものがございましたら用意できます。
メッセージでお声かけてください。
お待たせしています。
ミラノから帰国しました。
ブログに写真追加しました。

申し込みフォームまたは
ボタンを多めで途中でも押せるような
ランディングページをお願いいたします。

初心者でもわかりやすい、
目に見えて流れがわかるページでお願いいたします。

そろそろ決めていきたいと思っています。
フィーリングが合うデザイナーさんの
素敵な作品をお待ちしています。
どうぞよろしくお願いいたします。

良いデザインばかりだったので
迷いましたが、ずっと使えそうなデザインのものにしました。

素晴らしいご提案をありがとうございました!
また、素敵なデザインをよろしくお願いいたします。

```html
<!DOCTYPE html>
<html lang="ja">
<head>
<meta charset="utf-8">
<title>ロゴ意匠 | 書家 早瀬雪乃</title>
<link rel="stylesheet" href="https://fonts.googleapis.com/css2?family=Shippori+Mincho:wght@400;600;700&display=swap">
<style>
:root{
  --sakura:#d98aa9;
  --beni:#c9184c;
  --yamabuki:#efc23d;
  --wakatake:#5ba97f;
  --sora:#3d9bd9;
  --fuji:#8c5aa9;
  --sumi-fuji:#4d2d63;
  --shiro:#ffffff;
  --sumi:#2a2228;
  --shu:#d2233a;
  --paper:#f4efe8;
}
*{margin:0;padding:0;box-sizing:border-box}
html,body{width:1200px;height:4056px;overflow:hidden}
body{position:relative;font-family:"Shippori Mincho",serif;color:var(--shiro)}
.section{position:absolute;left:0;width:1200px}
.abs{position:absolute}
.tab{position:absolute;left:1060px;width:96px;background:var(--shiro);border:2px solid var(--sumi);color:var(--sumi);
  writing-mode:vertical-rl;font-size:40px;font-weight:600;letter-spacing:6px;padding:18px 0;display:flex;align-items:center;justify-content:flex-start}
.tab .seal{position:absolute;right:-26px;bottom:-8px;writing-mode:vertical-rl;background:var(--shu);color:var(--shiro);font-size:12px;padding:4px 2px;letter-spacing:1px}
.fill{position:absolute}
p{line-height:1.8}

/* hero */
.hero{top:0;height:560px;background:var(--sakura)}
.hero-title{position:absolute;top:100px;width:100%;text-align:center;font-size:64px;letter-spacing:40px;font-weight:600}
.hero-lead{position:absolute;top:270px;width:100%;text-align:center;font-size:32px;letter-spacing:4px}
.hero-text{position:absolute;top:350px;left:240px;width:720px;font-size:16px}

/* profile */
.profile{top:560px;height:420px;background:var(--beni)}
.profile-name{position:absolute;top:50px;left:440px;font-size:30px;letter-spacing:4px}
.profile-name small{font-size:16px;margin-right:14px}
.profile-text{position:absolute;top:110px;left:440px;width:580px;font-size:15px}

/* world */
.world{top:980px;height:840px;background:var(--yamabuki)}
.world-head{position:absolute;top:80px;left:440px;font-size:32px;letter-spacing:3px}
.world-head small{font-size:16px;margin-right:12px}
.exhibit-list{position:absolute;top:150px;left:440px;list-style:none;font-size:15px;line-height:27px}
.exhibit-list span{display:inline-block;width:96px}

/* works */
.works{top:1820px;height:860px;background:var(--wakatake)}
.work{position:absolute;width:140px;text-align:center;font-size:14px}
.work .thumb{margin-top:10px;width:140px;height:110px;background:linear-gradient(160deg,var(--paper),#ddd3c6)}

/* studio */
.studio{top:2680px;height:720px;background:var(--sora)}
.studio-col{position:absolute;top:520px;width:400px}
.studio-col h3{font-size:20px;font-weight:600;margin-bottom:8px;letter-spacing:2px}
.studio-col p{font-size:14px}

/* contact */
.contact{top:3400px;height:600px;background:var(--fuji)}
.share{position:absolute;left:80px;width:56px;height:56px;background:var(--shiro);border-radius:6px}
.field-label{position:absolute;font-size:15px}
.field{position:absolute;height:40px;background:var(--shiro);border-radius:3px}
.check{position:absolute;font-size:15px;display:flex;align-items:center;gap:8px}
.check i{display:inline-block;width:16px;height:16px;background:var(--shiro);border-radius:2px}
.submit{position:absolute;left:240px;top:540px;width:760px;height:44px;background:var(--sumi-fuji);color:var(--shiro);
  font-size:18px;letter-spacing:14px;display:flex;align-items:center;justify-content:center}
.footer{top:4000px;height:56px;background:var(--sumi-fuji);font-size:12px;text-align:center;line-height:56px;letter-spacing:1px}
</style>
</head>
<body>

<section class="section hero">
  <div class="fill" role="img" aria-label="縦書きの書道ロゴ作品" style="left:70px;top:250px;width:90px;height:200px;background:linear-gradient(180deg,#c4708f,#b35a7c);opacity:.55"></div>
  <h1 class="hero-title">ロゴ意匠</h1>
  <p class="hero-lead">日本の美、日本の字、日本の印。</p>
  <p class="hero-text">筆で書く文字には、ひとつとして同じ形がありません。書家が一枚ずつ心をこめて書き上げた文字を、企業や店舗、商品の顔となるロゴへ仕立てます。伝統の書と現代のデザインが出会うとき、日本の美しさが新しい印となって息づきます。</p>
  <div class="tab" style="top:20px;height:250px">ロゴデザイン<span class="seal">雪乃</span></div>
</section>

<section class="section profile">
  <div class="fill" role="img" aria-label="袴姿で筆を持つ書家のプロフィール写真" style="left:160px;top:130px;width:240px;height:240px;background:linear-gradient(160deg,#c9b8a8,#5a4a48)"></div>
  <h2 class="profile-name"><small>女流書家</small>早瀬雪乃</h2>
  <p class="profile-text">幼少より書に親しみ、師のもとで二十余年研鑽を積む。国内外の展覧会に多数出品し、受賞多数。海外ではミラノ、パリ、ニューヨークなどで揮毫公演を行い、日本の書の魅力を伝える。企業ロゴ、商品題字、店舗看板など幅広い分野で筆耕を手がけ、書道教室を主宰。伝統を大切にしながら、暮らしに寄り添う新しい書のかたちを探求している。</p>
  <div class="tab" style="top:20px;height:250px">プロフィール<span class="seal">雪乃</span></div>
</section>

<section class="section world">
  <div class="fill" role="img" aria-label="白い墨で書かれた「花」の大字作品" style="left:120px;top:180px;width:260px;height:420px;background:radial-gradient(ellipse at 50% 45%,rgba(255,255,255,.75),rgba(255,255,255,0) 70%)"></div>
  <h2 class="world-head"><small>過去3年間で行った</small>海外展示</h2>
  <ul class="exhibit-list">
    <li><span>2015年10月</span>イタリア・ミラノ 日本文化交流展 出展</li>
    <li><span>2015年9月</span>フランス・パリ 書と現代美術展 招待出品</li>
    <li><span>2015年6月</span>アメリカ・ニューヨーク 揮毫公演</li>
    <li><span>2015年5月</span>シンガポール 日本の美展 出展</li>
    <li><span>2015年3月</span>台湾・台北 国際書画交流展 出品</li>
    <li><span>2014年11月</span>ドイツ・ベルリン 和の文化祭 揮毫公演</li>
    <li><span>2014年10月</span>フランス・パリ 日本文化サロン展 出展</li>
    <li><span>2014年8月</span>イギリス・ロンドン 書の芸術展 出品</li>
    <li><span>2014年7月</span>スペイン・バルセロナ 墨の表現展 出展</li>
    <li><span>2014年5月</span>アメリカ・ロサンゼルス 書道展 出品</li>
    <li><span>2014年4月</span>香港 アジア芸術フェア 出展</li>
    <li><span>2014年2月</span>オーストラリア・シドニー 和文化展 出品</li>
    <li><span>2013年12月</span>イタリア・ローマ 日伊交流書展 出展</li>
    <li><span>2013年10月</span>ベルギー・ブリュッセル 書画展 出品</li>
    <li><span>2013年9月</span>フランス・リヨン 揮毫公演</li>
    <li><span>2013年7月</span>カナダ・トロント 日本美術展 出展</li>
    <li><span>2013年5月</span>韓国・ソウル 国際書芸展 出品</li>
    <li><span>2013年3月</span>タイ・バンコク 日本の書展 出展</li>
    <li><span>2013年1月</span>アメリカ・ハワイ 新春書初め公演</li>
  </ul>
  <div class="tab" style="top:20px;height:250px">世界中で活躍<span class="seal">雪乃</span></div>
</section>

<section class="section works">
  <div class="work" style="left:160px;top:80px">ロゴ<div class="thumb" role="img" aria-label="書道ロゴ作品"></div></div>
  <div class="work" style="left:320px;top:80px">看板<div class="thumb" role="img" aria-label="看板題字作品"></div></div>
  <div class="work" style="left:480px;top:80px">題字<div class="thumb" role="img" aria-label="題字作品"></div></div>
  <div class="work" style="left:640px;top:80px">店舗<div class="thumb" role="img" aria-label="店舗ロゴ作品"></div></div>
  <div class="work" style="left:160px;top:380px">商品名<div class="thumb" role="img" aria-label="商品名の書"></div></div>
  <div class="work" style="left:320px;top:380px">暖簾<div class="thumb" role="img" aria-label="暖簾の題字"></div></div>
  <div class="work" style="left:480px;top:380px">表札<div class="thumb" role="img" aria-label="表札の書"></div></div>
  <div class="work" style="left:640px;top:380px">作品<div class="thumb" role="img" aria-label="インテリア書作品"></div></div>
  <div class="work" style="left:160px;top:628px">命名書<div class="thumb" role="img" aria-label="命名書作品"></div></div>
  <div class="tab" style="top:20px;height:250px">題字と筆耕<span class="seal">雪乃</span></div>
</section>

<section class="section studio">
  <div class="fill" role="img" aria-label="白い墨で大きく書かれた屋号の書" style="left:400px;top:110px;width:660px;height:340px;background:radial-gradient(ellipse at 50% 50%,rgba(255,255,255,.7),rgba(255,255,255,0) 70%)"></div>
  <div class="studio-col" style="left:160px">
    <h3>事業概要</h3>
    <p>ロゴ・題字・看板文字の制作、インテリア用書作品の制作販売、書道教室の運営を行っています。ご要望を丁寧に伺い、想いが伝わる一枚を書き上げます。</p>
  </div>
  <div class="studio-col" style="left:640px">
    <h3>揮毫公演</h3>
    <p>国内外のイベントや式典で、大筆を用いた揮毫公演を行います。音楽や舞と合わせた演出も可能です。お気軽にご相談ください。</p>
  </div>
  <div class="tab" style="top:20px;height:250px">揮毫と教室<span class="seal">雪乃</span></div>
</section>

<section class="section contact">
  <div class="share" style="top:40px"></div>
  <div class="share" style="top:140px"></div>
  <div class="share" style="top:240px"></div>

  <div class="field-label" style="left:240px;top:40px">お名前</div>
  <div class="field" style="left:240px;top:64px;width:360px"></div>
  <div class="field-label" style="left:240px;top:120px">メールアドレス</div>
  <div class="field" style="left:240px;top:144px;width:360px"></div>
  <div class="field-label" style="left:240px;top:200px">TEL</div>
  <div class="field" style="left:240px;top:224px;width:360px"></div>
  <div class="field-label" style="left:240px;top:280px">郵便番号</div>
  <div class="field" style="left:240px;top:304px;width:360px"></div>
  <div class="field-label" style="left:240px;top:360px">ご質問・ご要望</div>
  <div class="field" style="left:240px;top:384px;width:760px;height:130px"></div>

  <div class="field-label" style="left:640px;top:40px">件名・タイトル</div>
  <div class="field" style="left:640px;top:64px;width:360px"></div>
  <div class="field-label" style="left:640px;top:120px">お問い合わせの種類</div>
  <div class="check" style="left:640px;top:156px"><i></i>ロゴ制作</div>
  <div class="check" style="left:820px;top:156px"><i></i>題字・看板</div>
  <div class="check" style="left:640px;top:196px"><i></i>作品購入</div>
  <div class="check" style="left:820px;top:196px"><i></i>書道教室</div>
  <div class="check" style="left:640px;top:236px"><i></i>揮毫公演</div>
  <div class="check" style="left:820px;top:236px"><i></i>その他</div>

  <div class="submit">確認</div>
  <div class="tab" style="top:20px;height:250px">お問い合わせ<span class="seal">雪乃</span></div>
</section>

<footer class="section footer">© All rights reserved 2015 Yukino Hayase</footer>

</body>
</html>
```